Bramblewick Co Leaflet. A5 2-sided Flyer for a UK Lawn Treatment Company

I need an A5 two-side leaflet / flyer designed for my Lawn Treatment company. The leaflet will be for door-drops so quick impact needed. Full colour, both sides. I provide lawn treatments to customers in the Exeter area of Devon. I would like to design to be clear, fresh and reflect the joy a good lawn and garden can bring.

Target Market(s)

Home Owners. 30-80 Years. Familys

Font styles to use
Sans Serif

Colors
9bcb3c
f78f20
ec1f27
33a6d7

Requirements
Must have
• Good front page picture
• Logo
• Contact details on front.
• Call to Action
• More details in Text file included in design.
Nice to have
• Clipart of a family / lady enjoying a lawn.

```html
<!DOCTYPE html>
<html lang="en">
<head>
<meta charset="utf-8">
<title>Bramblewick Co – A5 Leaflet</title>
<link rel="stylesheet" href="https://fonts.googleapis.com/css2?family=Roboto+Slab:wght@400&family=Open+Sans:ital,wght@0,400;0,700;1,400;1,700&family=Exo+2:ital,wght@1,600;1,700&family=Russo+One&display=swap">
<style>
:root{
  --page-bg:#e6e7e9;
  --ink:#2b2b2b;
  --tag-red:#e5242c;
  --bullet-red:#ec1f27;
  --forest:#244a34;
  --cta-yellow:#f5e61c;
  --sky-top:#4d86de;
  --sky-mid:#cfe6f7;
  --grass-light:#9bcb3c;
  --grass-mid:#5fa02a;
  --grass-dark:#2f6d1c;
  --orange:#f78f20;
  --leaf:#6cb33f;
  --white:#ffffff;
}
*{box-sizing:border-box;margin:0;padding:0}
html,body{width:1200px;height:1200px;overflow:hidden;background:var(--page-bg)}
.sheet{position:absolute;top:200px;width:555px;height:793px;overflow:hidden;box-shadow:0 6px 18px rgba(0,0,0,.25);font-family:"Open Sans",sans-serif;color:var(--ink)}
.front{left:30px}
.back{left:615px;background:var(--white)}

/* front */
.front-scene{position:absolute;inset:0 0 167px 0;background:linear-gradient(180deg,var(--sky-top) 0%,#8fbdf0 18%,var(--sky-mid) 45%,#eef6fb 70%,#d5e9a8 86%,var(--grass-mid) 100%)}
.headline{position:absolute;left:38px;top:56px;width:500px;font-family:"Roboto Slab",serif;font-size:33px;line-height:30px;color:var(--ink)}
.highlights{position:absolute;left:51px;top:152px;width:180px;font-family:"Roboto Slab",serif;font-size:14px;line-height:13px}
.highlights p{margin-bottom:14px}
.compare{position:absolute;left:252px;top:151px;width:264px;height:115px;background:rgba(255,255,255,.55);border-radius:12px;padding:13px 13px}
.compare-photo{position:absolute;top:13px;width:117px;height:88px;font-family:"Open Sans",sans-serif;font-style:italic;font-size:10px;color:#fff}
.compare-photo span{position:absolute;left:8px;bottom:4px}
.before{left:13px;background:linear-gradient(180deg,#2f4a25 0%,#55612e 45%,#a2983f 100%)}
.after{left:132px;background:linear-gradient(180deg,#33502a 0%,#4f8a2c 45%,#6fb33a 100%)}
.section{position:absolute;left:38px;width:482px}
.tag{display:inline-block;background:var(--tag-red);color:#fff;font-family:"Roboto Slab",serif;font-size:13.5px;line-height:19px;padding:0 22px 0 10px;clip-path:polygon(0 0,100% 0,calc(100% - 9px) 100%,0 100%);margin-left:-7px}
.section p{font-size:11.6px;line-height:17.5px;margin-top:6px;font-stretch:condensed;letter-spacing:-.15px}
.services{position:absolute;left:0;right:0;top:626px;height:89px;background:var(--white);display:flex;padding:17px 0 0 38px;gap:0}
.services ul{list-style:none;font-family:"Exo 2",sans-serif;font-style:italic;font-weight:600;font-size:12px;line-height:17.5px}
.services li{position:relative;padding-left:22px}
.services li::before{content:"";position:absolute;left:2px;top:6px;width:5px;height:5px;border-radius:50%;background:var(--bullet-red)}
.services ul:nth-child(1){width:145px}
.services ul:nth-child(2){width:146px}
.cta-bar{position:absolute;left:0;right:0;bottom:0;height:78px;background:var(--forest);color:#fff;display:flex;align-items:center;padding-left:51px}
.cta-line{font-family:"Exo 2",sans-serif;font-style:italic;font-weight:700;font-size:14px;line-height:14px;width:245px}
.cta-call{display:flex;align-items:center;color:var(--cta-yellow)}
.cta-call small{font-family:"Russo One",sans-serif;font-size:11px;line-height:11px;text-align:right;margin-right:4px}
.cta-call strong{font-family:"Russo One",sans-serif;font-weight:400;font-size:28px;letter-spacing:.3px}

/* back */
.back-scene{position:absolute;left:0;right:0;top:0;height:611px;background:linear-gradient(180deg,var(--grass-light) 0%,#7fbf32 40%,var(--grass-mid) 80%,var(--grass-dark) 100%)}
.testimonials{position:absolute;left:20px;top:64px;width:515px;height:422px;background:rgba(155,203,60,.55);border-radius:0 8px 8px 8px;padding:12px 16px 0 16px;color:#fff}
.testimonials-tab{position:absolute;left:20px;top:27px;height:37px;padding:12px 14px 0 17px;background:rgba(155,203,60,.55);border-radius:8px 8px 0 0;font-family:"Open Sans",sans-serif;font-weight:700;font-size:14.5px;color:#fff}
.quote{font-style:italic;font-size:11.7px;line-height:17.4px;text-align:justify;margin-bottom:17px;letter-spacing:-.2px}
.quote b{font-weight:700}
.photo-strip{position:absolute;left:0;right:0;top:511px;height:145px;display:flex;gap:2px;background:#fff}
.photo-strip div{height:100%}
.strip-1{width:142px;background:linear-gradient(180deg,#2d4a22,#5f9a34 55%,#7cbc3e)}
.strip-2{width:190px;background:linear-gradient(180deg,#4d6a3a,#3f7d28 55%,#6aab34)}
.strip-3{flex:1;background:linear-gradient(180deg,#6b7a5a,#5e8f30 50%,#8cc343)}
.contact-band{position:absolute;left:0;right:0;bottom:0;height:137px;background:linear-gradient(180deg,#f3f3f3,#fff 20%)}
.brand{position:absolute;left:34px;top:54px;display:flex;align-items:center;gap:7px;font-family:"Open Sans",sans-serif;font-weight:700;font-size:17px;color:var(--forest)}
.brand i{width:12px;height:12px;border-radius:50%;background:var(--leaf)}
.contacts{position:absolute;left:200px;top:27px;font-family:"Open Sans",sans-serif}
.contacts small{display:block;font-style:italic;font-size:10px;line-height:13px;color:#333}
.contacts .phone{font-weight:700;font-size:20px;line-height:24px;color:var(--orange)}
.contacts .mobile{font-weight:700;font-size:20px;line-height:24px;color:var(--leaf)}
.web-pill{position:absolute;right:0;top:45px;width:190px;height:48px;background:linear-gradient(90deg,var(--leaf),var(--grass-light));border-radius:10px 0 0 10px;padding:7px 0 0 15px;color:#fff;box-shadow:0 3px 6px rgba(0,0,0,.15)}
.web-pill small{display:block;font-family:"Exo 2",sans-serif;font-style:italic;font-weight:600;font-size:10px;line-height:12px}
.web-pill strong{font-family:"Exo 2",sans-serif;font-style:italic;font-weight:700;font-size:16px}
</style>
</head>
<body>

<section class="sheet front" aria-label="Leaflet front">
  <div class="front-scene" role="img" aria-label="Bright blue sky fading over a lush green lawn"></div>
  <h1 class="headline">Treatments and advice to keep your lawn looking nice.</h1>
  <div class="highlights">
    <p>Brand new to the area!</p>
    <p>8 Years experience maintaining the finest lawns of Cheshire</p>
    <p>Complete Satisfaction Guarantee</p>
  </div>
  <div class="compare">
    <div class="compare-photo before" role="img" aria-label="Lawn before treatment, patchy and yellowed"><span>Before</span></div>
    <div class="compare-photo after" role="img" aria-label="Same lawn after treatment, even and green"><span>After</span></div>
  </div>

  <div class="section" style="top:295px">
    <span class="tag">For a beautiful weed-free lawn</span>
    <p>Call Bramblewick Co today and start your journey to a wonderful, lush, green lawn you and your family can enjoy. Arrange a no-obligation lawn survey and quotation at a time to suit you. Call 01632 960482 now.</p>
  </div>
  <div class="section" style="top:381px">
    <span class="tag">I will understand your lawn</span>
    <p>Every lawn is unique. I take time to gain a comprehensive understanding of your lawn and its situation. I will also listen to you and understand your problems and your aspirations for your grass.</p>
  </div>
  <div class="section" style="top:468px">
    <span class="tag">Your lawn treatments</span>
    <p>I will creat a custom treatment programme tailored to your lawn. I may also recommend some remedial treatments to correct any existing problems. There is no contract to sign. I guarantee all treatments.</p>
  </div>
  <div class="section" style="top:552px">
    <span class="tag">Industry-leading lawn care</span>
    <p>I have 8 years of experience in the leading edge of domestic lawn care. I have a comprehensive range of treatments including:</p>
  </div>

  <div class="services">
    <ul><li>Scarification</li><li>Aeration</li><li>Moss Control</li></ul>
    <ul><li>Overseeding</li><li>Top Dressing</li><li>Lawn Repairs</li></ul>
    <ul><li>Fertilisation &amp; Weed Control</li><li>Pest and Disease Management</li><li>Special Event Preparation</li></ul>
  </div>

  <div class="cta-bar">
    <p class="cta-line">Save time and money and leave your lawn to an expert.</p>
    <div class="cta-call"><small>Call<br>Today</small><strong>01632 960482</strong></div>
  </div>
</section>

<section class="sheet back" aria-label="Leaflet back">
  <div class="back-scene" role="img" aria-label="Close-up of long green grass blades"></div>
  <div class="testimonials-tab">TESTIMONIALS</div>
  <div class="testimonials">
    <p class="quote">Thank you for keeping our lawn in great shape for so long, I've been really pleased with how it has looked since you took care of it. - <b>Owen</b></p>
    <p class="quote">My lawn has never looked better since the day that you started to look after it for me. - <b>Mrs. Pell</b></p>
    <p class="quote">We are so grateful for your skill over the years. We've seen our lawn thrive and you changed a neglected difficult garden to one that everyone comments on. - <b>Carys</b></p>
    <p class="quote">Thank you for the lawn service you have provided over the years. It is reassuring to have you come round as I know you carried out the service as promised unlike other lawn service companies I have dealt with. - <b>Martin</b></p>
    <p class="quote">We have very much appreciated your service over the last four years, and especially value your reliability and perennial cheerfulness! - <b>Rowan</b></p>
    <p class="quote">It has been a pleasure to do business with you over the last few years and the lawn you leave us with is infinitely healthier and more attractive than the lawn you inherited! - <b>Hilary</b></p>
    <p class="quote">Your company have been fantastic. Reliable, good advice, effective treatments and you are very knowledgeable about lawns. You really do know what you are talking about! Cannot recommend you highly enough. - <b>Martin</b></p>
  </div>

  <div class="photo-strip">
    <div class="strip-1" role="img" aria-label="Striped mown lawn bordered by shrubs"></div>
    <div class="strip-2" role="img" aria-label="Curving striped lawn beside a gravel path and house"></div>
    <div class="strip-3" role="img" aria-label="Neat garden lawn with potted plants and a fence"></div>
  </div>

  <div class="contact-band">
    <div class="brand"><i></i>Bramblewick Co</div>
    <div class="contacts">
      <small>Call today on</small>
      <div class="phone">01632 960482</div>
      <small>or text</small>
      <div class="mobile">07700 900318</div>
    </div>
    <div class="web-pill"><small>to book your lawn survey</small><strong>bramblewick.co.uk</strong></div>
  </div>
</section>

</body>
</html>
```